MORLIVEX Hemp based Pet Brand that growns it's own premium hemp and creates amazing pet products.

We need packaging designed for a new company based in South West Florida. We grow our own hemp with our other company Crest 4 Vale and use the harvest to make our hemp based pet products. Our initial products are pet treats that include Soft Chews and Calming Chews. The bags come in two different sizes. Regular bag being 7x10.25 inches and Small bag 4.25X6.25 inches. We also need a tincture box and label created. We want packaging that will catch the eye of the consumer and colors that compliment our logo. Dropper label size is 4x1.75 inches and the milligram of CBD is 1500. We have attached our manufacturers packaging and would like you to coppy everything other than their overall design and logo. Use default UPC and QR code, which we can replace later in the Ai file. Please see all the attached documents and please ask me if you have any questions. The final design should communicate a premium product that stand our from the rest. Something that catches the eye of the consumer by its premium appearance. Packaging is everything so I hope you can use your creative skills to create something special!

Target Market(s)

Pet owners

Font styles to use
Serif
Sans Serif

Colors
0054AA
0677BA
7BADD7
CADEEF
E8F1F8
0094D4
00A9DD
6FCCEA
C7EBF8
E9F6FB
EE7325
F08F49
F5BC92
FAE3D3
FDF4ED

Requirements
Must have
• Stand out design. Premium feel. Imagine shopping for something for your pet and seeing a brand that POPS and just looks like a good product because the packaging is so good.
Nice to have
• Modern mature feel
Should not have
• Cartoony feeling. Do not use baby blue everywhere. Do not include pictures of people in the packaging

```html
<!DOCTYPE html>
<html lang="en">
<head>
<meta charset="utf-8">
<title>MORLIVEX Calming Chews – Pouch Front and Back</title>
<link href="https://fonts.googleapis.com/css2?family=Oswald:wght@500;700&family=Roboto:wght@400;500&display=swap" rel="stylesheet">
<style>
  :root {
    --pouch-top: #00a9dd;
    --pouch-bottom: #0094d4;
    --pouch-line: #0677ba;
    --ink: #1f2a33;
    --orange: #f08f49;
    --orange-deep: #ee7325;
    --cream: #fdf4ed;
    --peach: #fae3d3;
    --white: #ffffff;
    --stage: #f7f8f9;
  }
  * { box-sizing: border-box; margin: 0; padding: 0; }
  html, body { width: 1200px; height: 900px; overflow: hidden; background: var(--stage); }
  body { position: relative; font-family: "Roboto", Arial, sans-serif; color: var(--ink); }

  .pouch {
    position: absolute; top: 170px; width: 330px; height: 560px;
    background: linear-gradient(170deg, var(--pouch-top), var(--pouch-bottom));
    border-radius: 18px 18px 4px 4px;
    overflow: hidden;
  }
  .pouch--back { left: 250px; }
  .pouch--front { left: 620px; }
  .zipper {
    position: absolute; left: 0; right: 0; top: 44px; height: 18px;
    border-top: 2px solid var(--pouch-line); border-bottom: 2px solid var(--pouch-line);
  }

  /* back */
  .back-content { position: absolute; left: 26px; right: 22px; top: 120px; }
  .back-heading { font-family: "Oswald", Arial, sans-serif; font-weight: 700; font-size: 15px; letter-spacing: .2px; }
  .ingredients-list { font-size: 8.5px; margin: 6px 0 14px; }
  .back-copy { font-size: 8.5px; line-height: 1.45; margin-top: 6px; }
  .info-table { display: flex; border: 1.5px solid var(--ink); margin-top: 14px; }
  .dosage { flex: 1.1; padding: 8px; border-right: 1.5px solid var(--ink); }
  .dosage-title { font-family: "Oswald", Arial, sans-serif; font-weight: 500; font-size: 13px; line-height: 1.2; margin-bottom: 6px; }
  .dosage-row { font-size: 11px; line-height: 1.4; }
  .nutrition { flex: 1; }
  .nutrition-title { font-family: "Oswald", Arial, sans-serif; font-weight: 500; font-size: 12px; padding: 5px 6px; border-bottom: 1.5px solid var(--ink); }
  .nutrition-row { display: flex; justify-content: space-between; font-size: 9px; padding: 4px 6px; border-bottom: 1px solid var(--ink); }
  .nutrition-row:last-child { border-bottom: none; }
  .disclaimer { font-size: 7.5px; line-height: 1.4; margin-top: 10px; }
  .back-marks { display: flex; align-items: center; gap: 14px; margin-top: 18px; padding-left: 20px; }
  .brand-mark { display: flex; align-items: center; gap: 5px; font-family: "Oswald", Arial, sans-serif; font-weight: 700; font-size: 12px; color: var(--ink); }
  .brand-dot { width: 12px; height: 12px; border-radius: 50%; background: var(--orange); }
  .cert-badge { width: 34px; height: 34px; border-radius: 50%; background: #6aa86a; }
  .agency-badge { width: 50px; height: 24px; background: var(--white); border-radius: 2px; }

  /* front */
  .front-brand {
    position: absolute; top: 100px; left: 0; right: 0;
    display: flex; justify-content: center; align-items: center; gap: 8px;
    font-family: "Oswald", Arial, sans-serif; font-weight: 700; font-size: 24px; letter-spacing: 2px;
  }
  .front-brand .brand-dot { width: 18px; height: 18px; }
  .product-name {
    position: absolute; top: 200px; left: 0; right: 0; text-align: center;
    font-family: "Oswald", Arial, sans-serif; font-weight: 700; font-size: 38px; letter-spacing: .5px;
  }
  .pet-illustration {
    position: absolute; left: 24px; right: 24px; top: 268px; bottom: 0;
    border-radius: 120px 120px 0 0;
    background: linear-gradient(180deg, var(--white), var(--cream));
  }
  .product-type {
    position: absolute; top: 375px; left: 0; right: 0; text-align: center;
    font-family: "Oswald", Arial, sans-serif; font-weight: 700; font-size: 40px; color: var(--orange-deep); line-height: 1;
  }
  .product-subtype {
    position: absolute; top: 424px; left: 0; right: 0; text-align: center;
    font-size: 14px; letter-spacing: 2.5px;
  }
  .net-weight { position: absolute; bottom: 40px; left: 0; right: 0; text-align: center; font-size: 9px; }
</style>
</head>
<body>

<section class="pouch pouch--back">
  <div class="zipper"></div>
  <div class="back-content">
    <h2 class="back-heading">INGREDIENTS:</h2>
    <p class="ingredients-list">Rolled Oats, Hemp Plup, Peanut Butter, Honey, Indica Distillate.</p>
    <h2 class="back-heading">CALMING CHEWS</h2>
    <p class="back-copy">Our canine calming chews are a vital part of your dogs daily health and nutrition. Our proprietary blend of organic hemp, with naturally occurring CBDa, provides the most effective way to supplement the health and wellness of your pets. Pain, inflammation, anxiety, skin/coat health and restfulness are important to a dog's overall health.</p>
    <div class="info-table">
      <div class="dosage">
        <p class="dosage-title">TREAT YOUR BEST<br>FRIEND AM/PM</p>
        <p class="dosage-row">2-25 lbs 1/2 chew</p>
        <p class="dosage-row">&lt; 50 lbs- 1 chew</p>
        <p class="dosage-row">&gt; 50 lbs - 2 chews</p>
      </div>
      <div class="nutrition">
        <p class="nutrition-title">Nutrition Facts</p>
        <p class="nutrition-row"><span>Fat:</span><span>0.5 g</span></p>
        <p class="nutrition-row"><span>Carb:</span><span>2 g</span></p>
        <p class="nutrition-row"><span>Protein:</span><span>1 g</span></p>
        <p class="nutrition-row"><span>Fiber:</span><span>0.3 g</span></p>
      </div>
    </div>
    <p class="disclaimer">• These statements have not been evaluated by the Food and drugs Administration. This product is not intended to diagnose, treat, cure or prevent any disease.</p>
    <div class="back-marks">
      <div class="brand-mark"><span class="brand-dot"></span>MORLIVEX</div>
      <div class="cert-badge" role="img" aria-label="Manufacturing certification badge"></div>
      <div class="agency-badge" role="img" aria-label="Regulatory agency mark"></div>
    </div>
  </div>
</section>

<section class="pouch pouch--front">
  <div class="zipper"></div>
  <div class="front-brand"><span class="brand-dot"></span>MORLIVEX</div>
  <h1 class="product-name">CALMING CHEWS</h1>
  <div class="pet-illustration" role="img" aria-label="Dog and cat silhouette illustration with a hemp leaf"></div>
  <p class="product-type">CBD HEMP</p>
  <p class="product-subtype">Treatment</p>
  <p class="net-weight">Net WT. 10.5 oz</p>
</section>

</body>
</html>
```